Webdesign für Zahnarztpraxis
Zielgruppe
Zahnarztpraxis
Aufgabenstellung
- Klares und übersichtliches Desgin
- Nicht zu verspielt
- Informativ
- Leichte Naviagtion
- Das Design der alten Webseite soll NICHT kopiert werden
- Die Farben Blau und Grün aus dem Logo sollen sich wiederfinden
- Designbeispiele, die dem Kunden gefallen sind https://www.kolbeck-mirowski-zahnarztpraxis.de/ und https://www.praxisolwing.de/

```html
<!DOCTYPE html>
<html lang="de">
<head>
<meta charset="utf-8">
<title>Zahnarztpraxis Wendholt – Talbrück-Oberau</title>
<link rel="stylesheet" href="https://fonts.googleapis.com/css2?family=Inter:wght@400;500;600;700&display=swap">
<style>
  :root{
    --blue:#1e9bd7;
    --green:#7cc043;
    --ink:#243447;
    --text:#2b2f36;
    --muted:#5a6676;
    --white:#ffffff;
    --line:#d6e4ee;
    --dark:#1b1b1b;
  }
  *{box-sizing:border-box;margin:0;padding:0}
  html,body{width:1200px;height:766px;overflow:hidden}
  body{font-family:"Inter",Arial,sans-serif;color:var(--text);background:var(--white);position:relative}

  .site-header{position:absolute;left:0;top:0;width:1200px;height:64px;background:var(--white);border-bottom:1px solid #e4e9ee}
  .brand{position:absolute;left:72px;top:21px;display:flex;align-items:center;gap:6px;white-space:nowrap}
  .brand-dot{width:10px;height:10px;border-radius:50%;background:var(--green)}
  .brand-name{font-size:16px;font-weight:600;color:var(--blue);line-height:20px}
  .practice{position:absolute;left:180px;top:17px;white-space:nowrap}
  .practice-name{font-size:14px;font-weight:500;color:var(--blue);line-height:18px}
  .practice-place{font-size:10.5px;color:var(--muted);line-height:14px}
  .nav-link{position:absolute;top:24px;font-size:13.5px;line-height:18px;color:var(--text);white-space:nowrap}
  .nav-praxis{left:578px}
  .nav-leistungen{left:688px}
  .nav-labor{left:780px}
  .nav-team{left:873px}
  .nav-kontakt{left:929px}
  .cta-appointment{position:absolute;left:999px;top:17px;width:141px;height:31px;border-radius:4px;background:var(--blue);color:var(--white);font-size:12.5px;font-weight:600;display:flex;align-items:center;justify-content:center;white-space:nowrap}

  .notice-band{position:absolute;left:0;top:65px;width:1200px;height:159px;background:linear-gradient(90deg,#e9f5fc,#eef7f8 60%,#f1f8ec);border-bottom:1px solid var(--line)}
  .notice{position:absolute;left:63px;top:28px;width:1076px;height:108px;background:var(--white);border:2px solid var(--blue);border-radius:5px}
  .notice-icon{position:absolute;left:15px;top:14px}
  .notice-title{position:absolute;left:40px;top:14px;font-size:16px;font-weight:500;color:var(--muted)}
  .notice-body{position:absolute;left:40px;top:51px;width:1010px;font-size:14px;line-height:23px;color:var(--text)}
  .notice-body b{font-weight:700}

  .hero{position:absolute;left:0;top:224px;width:1200px;height:542px;background:linear-gradient(160deg,#eaf6fd 0%,#f8fcfe 45%,#ffffff 70%)}
  .hero-title{position:absolute;left:35px;top:142px;font-size:39px;line-height:44px;font-weight:500;color:var(--ink);letter-spacing:-0.5px;white-space:nowrap}
  .hero-lead{position:absolute;left:35px;top:247px;width:470px;font-size:16px;line-height:25px;color:var(--muted)}
  .btn{position:absolute;top:325px;height:42px;border-radius:4px;color:var(--white);font-size:14.5px;font-weight:500;display:flex;align-items:center;justify-content:center;gap:9px;white-space:nowrap}
  .btn-call{left:35px;width:152px;background:var(--blue)}
  .btn-map{left:201px;width:179px;background:var(--green)}
  .team-photo{position:absolute;left:623px;top:72px;width:545px;height:364px;border-radius:12px;background:linear-gradient(180deg,#6f8f5a 0%,#9fb88a 35%,#e8ecef 60%,#d9dfe3 85%,#5f7d46 100%);box-shadow:0 14px 30px rgba(0,0,0,.18)}
  .help{position:absolute;left:1163px;top:727px;width:28px;height:28px;border-radius:50%;background:var(--dark);color:var(--white);font-size:13px;display:flex;align-items:center;justify-content:center}
</style>
</head>
<body>
  <header class="site-header">
    <div class="brand"><span class="brand-dot"></span><span class="brand-name">Wendholt</span></div>
    <div class="practice">
      <div class="practice-name">Zahnarztpraxis Wendholt</div>
      <div class="practice-place">Talbrück-Oberau</div>
    </div>
    <nav>
      <span class="nav-link nav-praxis">Unsere Praxis</span>
      <span class="nav-link nav-leistungen">Leistungen</span>
      <span class="nav-link nav-labor">Praxislabor</span>
      <span class="nav-link nav-team">Team</span>
      <span class="nav-link nav-kontakt">Kontakt</span>
    </nav>
    <div class="cta-appointment">Termin vereinbaren</div>
  </header>

  <section class="notice-band">
    <div class="notice">
      <svg class="notice-icon" width="14" height="14" viewBox="0 0 14 14" aria-hidden="true">
        <circle cx="7" cy="7" r="6" fill="none" stroke="#2b2f36" stroke-width="1.3"/>
        <line x1="7" y1="3.8" x2="7" y2="7.6" stroke="#2b2f36" stroke-width="1.4" stroke-linecap="round"/>
        <circle cx="7" cy="9.9" r="0.8" fill="#2b2f36"/>
      </svg>
      <div class="notice-title">Wichtige Information für unsere Patienten</div>
      <p class="notice-body"><b>Liebe Patienten,</b> in der Zeit von <b>xx.xx.2025 - einschließlich xx.xx.2025</b> bleibt unsere Praxis geschlossen. Die Vertretung in dieser Zeit übernimmt <b>Frau/Herr …</b> Bitte melden Sie sich im Vorfeld telefonisch an.</p>
    </div>
  </section>

  <section class="hero">
    <h1 class="hero-title">Ihre Zahngesundheit in den<br>besten Händen</h1>
    <p class="hero-lead">Praxis &amp; Dentallabor in Talbrück-Oberau. Prävention und Individualprophylaxe in jeder Altersgruppe!</p>
    <div class="btn btn-call">
      <svg width="17" height="17" viewBox="0 0 24 24" fill="none" stroke="#fff" stroke-width="1.8" stroke-linejoin="round" aria-hidden="true"><path d="M5 3h4l2 5-2.5 1.5a11 11 0 0 0 6 6L16 13l5 2v4a2 2 0 0 1-2 2A16 16 0 0 1 3 5a2 2 0 0 1 2-2z"/></svg>
      Jetzt anrufen
    </div>
    <div class="btn btn-map">
      <svg width="16" height="17" viewBox="0 0 24 24" fill="none" stroke="#fff" stroke-width="1.8" aria-hidden="true"><path d="M12 22s-7-7-7-12a7 7 0 0 1 14 0c0 5-7 12-7 12z"/><circle cx="12" cy="10" r="2.5"/></svg>
      So finden Sie uns
    </div>
    <div class="team-photo" role="img" aria-label="Gruppenfoto des Praxisteams in weißer Kleidung vor Bäumen und Sträuchern im Grünen"></div>
  </section>

  <div class="help">?</div>
</body>
</html>
```